Clay Sparrow- Hand made fashion accessories

Clay sparrow is a new business that will be selling hand made fashion accessories for women such as bags, baskets, knecklaces etc. The items are all hand made from Africa. I would like natural colors leaning more to the cardboard rustic look. I would like the card to look simple but elegant at the same time.

Industry/Entity Type

Business

Contact Information for Business Card

www.claysparrow-example.com.au
sales@claysparrow-example.com.au
Tel: 0452867310

Font styles to use
Decorative
Script

Requirements
Must have
• Earthy and rustic colours. Straw, cardboard etc. Fine black cursive print. One side of card only name
• second side website, email and tel.
Should not have
• No need to have any description of what business sells or does. No pictures of anything.

```html
<!DOCTYPE html>
<html lang="en">
<head>
<meta charset="UTF-8">
<title>Clay Sparrow – Business Card</title>
<link href="https://fonts.googleapis.com/css2?family=Pinyon+Script&family=Questrial&display=swap" rel="stylesheet">
<style>
  :root {
    --backdrop: #e8e7e4;
    --kraft: #d09a62;
    --kraft-edge: #b98352;
    --ink: #6e3b1c;
    --ink-soft: #7a4522;
  }
  * { margin: 0; padding: 0; box-sizing: border-box; }
  html, body {
    width: 1200px;
    height: 1021px;
    overflow: hidden;
    background: var(--backdrop);
    font-family: "Questrial", sans-serif;
  }
  .canvas {
    width: 1200px;
    height: 1021px;
    display: flex;
    flex-direction: column;
    align-items: center;
    justify-content: center;
    gap: 60px;
  }
  .card {
    position: relative;
    width: 740px;
    height: 430px;
    background: var(--kraft);
    border: 1px solid var(--kraft-edge);
    box-shadow: 0 6px 18px rgba(0,0,0,0.12);
    color: var(--ink);
  }
  .brand {
    display: flex;
    align-items: center;
    gap: 18px;
    white-space: nowrap;
    color: var(--ink);
  }
  .brand-dot {
    width: 16px;
    height: 16px;
    border-radius: 50%;
    background: var(--ink);
    flex: none;
  }
  .brand-name {
    font-family: "Pinyon Script", cursive;
    font-weight: 400;
    line-height: 1.2;
  }
  .card-front .brand {
    position: absolute;
    left: 50%;
    top: 50%;
    transform: translate(-50%, -50%);
  }
  .card-front .brand-name { font-size: 72px; }
  .card-back .brand {
    position: absolute;
    left: 50%;
    top: 105px;
    transform: translateX(-50%);
  }
  .card-back .brand-name { font-size: 56px; }
  .card-back .brand-dot { width: 13px; height: 13px; }
  .contact-line {
    position: absolute;
    left: 36px;
    right: 36px;
    bottom: 46px;
    display: flex;
    justify-content: space-between;
    align-items: center;
    font-size: 15px;
    color: var(--ink-soft);
    letter-spacing: 0.3px;
  }
  .contact-item {
    display: flex;
    align-items: center;
    gap: 6px;
    white-space: nowrap;
  }
  .contact-icon {
    width: 14px;
    height: 14px;
    flex: none;
  }
</style>
</head>
<body>
<main class="canvas">
  <section class="card card-front" aria-label="Card front">
    <div class="brand">
      <span class="brand-dot"></span>
      <span class="brand-name">Clay Sparrow</span>
    </div>
  </section>

  <section class="card card-back" aria-label="Card back">
    <div class="brand">
      <span class="brand-dot"></span>
      <span class="brand-name">Clay Sparrow</span>
    </div>
    <div class="contact-line">
      <span class="contact-item">
        <svg class="contact-icon" viewBox="0 0 14 14" aria-hidden="true">
          <circle cx="7" cy="7" r="6" fill="none" stroke="currentColor" stroke-width="1"/>
          <ellipse cx="7" cy="7" rx="2.6" ry="6" fill="none" stroke="currentColor" stroke-width="1"/>
          <line x1="1" y1="7" x2="13" y2="7" stroke="currentColor" stroke-width="1"/>
        </svg>
        www.claysparrow-example.com.au
      </span>
      <span class="contact-item">
        <svg class="contact-icon" viewBox="0 0 14 14" aria-hidden="true">
          <rect x="1" y="3" width="12" height="8" fill="none" stroke="currentColor" stroke-width="1"/>
          <polyline points="1,3 7,8 13,3" fill="none" stroke="currentColor" stroke-width="1"/>
        </svg>
        sales@claysparrow-example.com.au
      </span>
      <span class="contact-item">
        <svg class="contact-icon" viewBox="0 0 14 14" aria-hidden="true">
          <path d="M2 5 Q2 2 7 2 Q12 2 12 5 L9.5 5.5 L9 4 L5 4 L4.5 5.5 Z" fill="currentColor"/>
          <rect x="3" y="7" width="8" height="5" rx="1" fill="none" stroke="currentColor" stroke-width="1"/>
        </svg>
        0452867310
      </span>
    </div>
  </section>
</main>
</body>
</html>
```